Marlowe Brisa Pale Ale Beer Label/Badge

We need a Beer Label designed for our first official beer to be launched under the Marlowe Brand!!
It will be a Pale Ale Called "Brisa Pale Ale"!

The Marlowe has the largest Craft Beer & Cider selection in the Geelong & Surf Coast region. With a funky location and a relaxed vibe, Marlowe prides itself on serving delicious, unique seasonal food paired with Australia's best Craft Beer. The marlowe is the perfect setting for a relaxed afternoon or evening with friends and can package an experience for larger groups or corporate bookings.

The Marlowe Tavern brand has been growing for over a year and a half and the first label needs to integrate the Marlowe Logo but at the same time bring a fresh, new and eye catching feel to it along with embracing the "Odysseus" story in which we will be naming future beers.

The story of Calypso is found via the following link
http://en.lorevault.example/wiki/Brisa_(legend)

We expect designers to research the Marlowe Tavern brand along with the all important Craft Beer Market and demographics. This will, potentially, be the start of many more labels to come for the winning designer!!

Requirements
Must have
• The original "O" needs to be integrated into the new logo and as much as the Greek mythology is being used it needs to be certain that this is an original Australian Craft Beer in the modern age!!
strong, modern & unique!!
Nice to have
• Logo could have a depiction of Calypso
Should not have
• tackiness or cheap!!

```html
<!DOCTYPE html>
<html lang="en">
<head>
<meta charset="utf-8">
<title>Marlowe Brisa Pale Ale – Label Design</title>
<link href="https://fonts.googleapis.com/css2?family=Oswald:wght@500;600&family=Bebas+Neue&family=Nothing+You+Could+Do&display=swap" rel="stylesheet">
<style>
  :root {
    --page: #e9e5dc;
    --paper: #fbfbfa;
    --rule: #e2e2e2;
    --ink: #3a3a3a;
    --red: #8f2620;
    --green: #b3c236;
    --art-light: #e6e4e0;
    --art-dark: #bdb9b2;
  }
  * { box-sizing: border-box; margin: 0; padding: 0; }
  html, body { width: 1200px; height: 900px; overflow: hidden; }
  body {
    background: var(--page);
    display: flex;
    align-items: center;
    justify-content: center;
    gap: 60px;
  }
  .label {
    --band: var(--red);
    position: relative;
    width: 360px;
    height: 560px;
    background: var(--paper);
    box-shadow: 0 2px 10px rgba(0,0,0,.12);
    overflow: hidden;
  }
  .label--green { --band: var(--green); }

  .label__head {
    position: absolute; inset: 0 0 auto 0; height: 224px;
    background: repeating-linear-gradient(to bottom, var(--paper) 0 6px, var(--rule) 6px 7px);
  }
  .brand {
    position: absolute; left: 28px; top: 58px;
    display: flex; align-items: center; gap: 10px;
  }
  .brand__dot { width: 30px; height: 30px; border-radius: 50%; background: var(--red); }
  .brand__name {
    font-family: "Oswald", sans-serif; font-weight: 600; font-size: 26px;
    letter-spacing: 1px; color: var(--red); text-transform: uppercase;
  }
  .label__art {
    position: absolute; left: 185px; top: 18px; width: 160px; height: 206px;
    background: linear-gradient(160deg, var(--art-light), var(--art-dark));
  }

  .label__band {
    position: absolute; left: 3px; right: 4px; top: 224px; height: 274px;
    background: var(--band);
  }
  .label__side {
    position: absolute; left: 14px; top: 224px; width: 40px; bottom: 0;
    background: var(--paper);
    display: flex; align-items: center; justify-content: center;
  }
  .label__side span {
    transform: rotate(90deg); white-space: nowrap;
    font-family: "Oswald", sans-serif; font-weight: 500; font-size: 19px;
    letter-spacing: 2px; color: var(--ink);
  }
  .title {
    position: absolute; left: 64px; top: 236px; right: 10px;
    font-family: "Bebas Neue", sans-serif; color: var(--paper);
    font-size: 84px; line-height: 72px; letter-spacing: 2px;
  }
  .maker {
    position: absolute; left: 64px; top: 418px; width: 222px; height: 74px;
    background: var(--paper);
    display: flex; flex-direction: column; align-items: center; justify-content: center;
    font-family: "Oswald", sans-serif; font-weight: 500; color: var(--red);
    text-transform: uppercase;
  }
  .maker__name { font-size: 30px; line-height: 32px; letter-spacing: 1px; }
  .maker__sub { font-size: 11px; letter-spacing: 2px; }
  .abv {
    position: absolute; left: 296px; top: 418px; width: 54px; height: 74px;
    background: var(--paper);
    display: flex; align-items: center; justify-content: center;
    font-family: "Oswald", sans-serif; font-weight: 600; font-size: 24px; color: var(--ink);
  }
  .origin {
    position: absolute; left: 64px; top: 512px;
    font-family: "Nothing You Could Do", cursive; font-size: 17px; color: var(--ink);
  }
</style>
</head>
<body>
  <article class="label label--red">
    <div class="label__head"></div>
    <div class="brand"><span class="brand__dot"></span><span class="brand__name">Marlowe</span></div>
    <div class="label__art" role="img" aria-label="Engraved-style illustration of Brisa in profile"></div>
    <div class="label__band"></div>
    <div class="label__side"><span>HANDCRAFTED BEER</span></div>
    <h1 class="title">Brisa<br>Pale Ale</h1>
    <div class="maker"><span class="maker__name">Marlowe</span><span class="maker__sub">Tavern + Brewery</span></div>
    <div class="abv">5%</div>
    <p class="origin">Mount Wirra, Victoria, Australia</p>
  </article>

  <article class="label label--green">
    <div class="label__head"></div>
    <div class="brand"><span class="brand__dot"></span><span class="brand__name">Marlowe</span></div>
    <div class="label__art" role="img" aria-label="Engraved-style illustration of Brisa in profile"></div>
    <div class="label__band"></div>
    <div class="label__side"><span>HANDCRAFTED BEER</span></div>
    <h1 class="title">Brisa<br>Pale Ale</h1>
    <div class="maker"><span class="maker__name">Marlowe</span><span class="maker__sub">Tavern + Brewery</span></div>
    <div class="abv">5%</div>
    <p class="origin">Mount Wirra, Victoria, Australia</p>
  </article>
</body>
</html>
```